Business Card Design Project

Hi. We need a new business card for Brightfield Partners, a consultancy that helps people with online marketing strategy and solutions.

We have a new logo and now need the info presented - front and back of business card.

FRONT

Logo

Online strategy, consulting and coaching
Varlo Admarket consulting
Search Engine Optimisation
Internet Lead Generation
Domain name broking

BACK

Tom Bradwell-Jones
+ 61 83215 9076
+ 61 (0) 418 536 207
tom@brightfieldpartners.com.au
www.brightfieldpartners.com.au

Talkora: tombradwelljones
PO Box 312, South Perth, Western Australia 6951

Target Market(s)

Business owners, corporates

Industry/Entity Type

Marketing

Requirements
Must have
• double sided
size: 86 x 54mm
supplied as one pdf with crop marks shown (+- 1mm, with 2-3 mm bleed)

```html
<!DOCTYPE html>
<html lang="en">
<head>
<meta charset="utf-8">
<title>Brightfield Partners – Business Card</title>
<link rel="stylesheet" href="https://fonts.googleapis.com/css2?family=Arimo:wght@400;700&family=Open+Sans:wght@700&display=swap">
<style>
  :root {
    --orange: #fd4d2a;
    --orange-text: #f47a1f;
    --blue: #1f78c8;
    --blue-deep: #1458b0;
    --ink: #2c3338;
    --page: #ffffff;
    --edge: #1a1a1a;
  }
  * { box-sizing: border-box; margin: 0; padding: 0; }
  html, body { width: 1200px; height: 1200px; overflow: hidden; background: var(--page); }
  body { position: relative; font-family: "Arimo", Arial, sans-serif; }

  .card {
    position: absolute;
    left: 206px;
    width: 776px;
    height: 438px;
    border: 1px solid var(--edge);
    background: var(--page);
    overflow: hidden;
  }
  .card--front { top: 86px; }
  .card--back { top: 582px; }

  .front-bands { position: absolute; inset: 0; width: 100%; height: 100%; }

  .brand {
    position: absolute;
    font-family: "Arimo", Arial, sans-serif;
    font-weight: 700;
    color: var(--blue-deep);
    line-height: 1;
    letter-spacing: -0.5px;
  }
  .brand__dot {
    display: inline-block;
    width: 0.7em; height: 0.7em;
    border-radius: 50%;
    background: var(--orange-text);
    margin-right: 0.25em;
    vertical-align: 0.05em;
  }
  .card--front .brand { left: 270px; top: 246px; width: 490px; text-align: center; font-size: 44px; }
  .front-url {
    position: absolute; left: 270px; top: 310px; width: 490px;
    text-align: center; font-weight: 700; font-size: 15px;
    letter-spacing: 3px; color: var(--blue-deep);
  }
  .card--back .brand { left: 48px; top: 70px; font-size: 40px; }
  .card--back .brand span { display: block; }

  .contact { position: absolute; list-style: none; }
  .contact li {
    position: absolute; left: 0; white-space: nowrap;
    font-weight: 700; font-size: 18px; line-height: 21px; color: var(--blue);
  }
  .contact svg { position: absolute; left: -36px; top: 0; width: 26px; height: 24px; }
  .contact--left { left: 79px; top: 0; }
  .contact--right { left: 480px; top: 0; }
  .contact .web { color: var(--orange-text); top: 260px; }
  .contact .post { top: 296px; }
  .contact .talkora { top: 356px; }
  .contact .mail { top: 296px; font-size: 17px; }
  .contact .phone { top: 328px; }

  .holder {
    position: absolute; left: 437px; top: 254px;
    font-family: "Open Sans", Arial, sans-serif; font-weight: 700;
    font-size: 26px; color: var(--orange);
  }

  .back-band { position: absolute; left: 0; bottom: 0; width: 100%; height: 26px; }
</style>
</head>
<body>

<section class="card card--front" aria-label="Card front">
  <svg class="front-bands" viewBox="0 0 776 438" preserveAspectRatio="none" aria-hidden="true">
    <polygon points="0,0 394,0 148,438 0,438" fill="var(--orange)"/>
    <polygon points="394,0 415,0 166,438 148,438" fill="var(--blue)"/>
  </svg>
  <div class="brand"><span class="brand__dot"></span>Brightfield Partners</div>
  <div class="front-url">brightfieldpartners.com.au</div>
</section>

<section class="card card--back" aria-label="Card back">
  <div class="brand"><span>Brightfield</span><span>Partners</span></div>

  <ul class="contact contact--left">
    <li class="web">
      <svg viewBox="0 0 24 24" aria-hidden="true"><g fill="none" stroke="var(--ink)" stroke-width="1.5"><circle cx="12" cy="12" r="10"/><ellipse cx="12" cy="12" rx="4.5" ry="10"/><line x1="2" y1="12" x2="22" y2="12"/><path d="M4 7h16M4 17h16"/></g></svg>
      www.brightfieldpartners.com.au
    </li>
    <li class="post">
      <svg viewBox="0 0 24 24" aria-hidden="true"><g fill="none" stroke="var(--ink)" stroke-width="1.6"><path d="M2 11 12 3l10 8"/><path d="M5 9v12h14V9"/><rect x="10" y="14" width="4" height="7"/><rect x="6.5" y="12" width="2.5" height="2.5"/><rect x="15" y="12" width="2.5" height="2.5"/></g></svg>
      PO Box 312, South Perth,<br>&nbsp;Western Australia 6951
    </li>
    <li class="talkora">
      <svg viewBox="0 0 24 24" aria-hidden="true"><circle cx="12" cy="12" r="10" fill="#35c3ee"/></svg>
      tombradwelljones
    </li>
  </ul>

  <div class="holder">Tom Bradwell-Jones</div>

  <ul class="contact contact--right">
    <li class="mail">
      <svg viewBox="0 0 26 24" aria-hidden="true"><rect x="1" y="5" width="24" height="15" fill="var(--ink)"/><path d="M1 5l12 9 12-9" fill="none" stroke="#fff" stroke-width="1.5"/></svg>
      tom@brightfieldpartners.com.au
    </li>
    <li class="phone">
      <svg viewBox="0 0 26 24" aria-hidden="true"><path d="M2 8c0-3 5-4 11-4s11 1 11 4v2h-5V8H7v2H2z" fill="var(--ink)"/><path d="M6 11h14l3 10H3z" fill="var(--ink)"/><circle cx="13" cy="16" r="2.5" fill="#fff"/></svg>
      + 61 83215 9076<br>+ 61 (0) 418 536 207
    </li>
  </ul>

  <svg class="back-band" viewBox="0 0 776 26" preserveAspectRatio="none" aria-hidden="true">
    <rect x="0" y="0" width="776" height="26" fill="var(--blue)"/>
    <polygon points="379,0 776,0 776,26 394,26" fill="var(--orange)"/>
  </svg>
</section>

</body>
</html>
```